Dental-Specific Brochure for IT Services

We are creating a brochure for IT services for local dental practices. Highlights should include:
- no contract / we earn your business on a month to month basis
- affordable pricing
- fast response times
- 25+ local dental practices
- predictable fixed-rate billing
Text should include:
Why Dental Practices Choose WFOL?At WFOL, we specialize in providing reliable, affordable, and high-quality IT solutions tailored specifically for dental offices. With over 25 local dental practices trusting us with their IT needs, we understand the unique challenges you face and offer solutions to keep your practice running smoothly.
What Sets WFOL Apart?
✅ No Contracts – We believe in earning your business every month. Stay because you want to, not because you have to.
✅ Affordable Pricing – Cost-effective solutions that fit your budget without sacrificing quality.
✅ Fast Response Times – When you need IT support, we’re there. Minimize downtime and keep your practice operational.
✅ Predictable Fixed-Rate Billing – No surprises, just straightforward pricing that makes budgeting easy.
✅ Proven Track Record – Over 25 dental practices in the area trust WFOL for their IT support.
✅ Expert Cybersecurity & Ransomware Protection – Advanced security measures to protect patient data and experience with HIPAA HITECH Act.
✅ Full Support for Practice Management Software – We work with Lumen Dental, Harborlink, Molvana, and other leading platforms.
Our IT Services for Dental Practices:
VoIP Phone Solutions – Reliable communication for your front desk and patient calls.
Managed IT Support – Proactive monitoring, maintenance, and troubleshooting to prevent downtime.
Cloud Solutions – Secure, scalable storage and software solutions for your practice.
Network & Wi-Fi Optimization – Fast, secure, and reliable internet for your office.
High-Speed Fiber Internet – Ensure fast and reliable connectivity to keep your practice running smoothly.
Let’s Get Started!
Join the growing number of dental practices that trust WFOL for their IT needs. Contact us today to schedule a consultation and see how we can help your practice thrive.
-
We would like contact info displayed similarly to how it is on the other brochure in the attachments. I will also be adding some more pictures to use; feel free to add in holding spots for pictures similar to what is in the example brochure.
Logo is in attachments along with current brochure.

```html
<!DOCTYPE html>
<html lang="en">
<head>
<meta charset="utf-8">
<title>WFOL – IT Services for Dental Practices</title>
<link href="https://fonts.googleapis.com/css2?family=Montserrat:wght@600;700;800&display=swap" rel="stylesheet">
<style>
  :root{
    --bg:#dcdcde;
    --green:#8cc63f;
    --navy:#0b1f8a;
    --navy-deep:#071566;
    --photo-a:#2a3f9e;
    --photo-b:#3d6fb0;
    --white:#ffffff;
  }
  *{box-sizing:border-box;margin:0;padding:0}
  html,body{width:1200px;height:1200px;overflow:hidden;background:var(--bg)}
  body{font-family:"Montserrat",sans-serif;color:var(--white)}
  .spread{position:absolute;left:60px;top:250px;width:1080px;height:700px;display:flex;box-shadow:0 20px 40px rgba(0,0,0,.18)}
  .page{position:relative;width:540px;height:700px;overflow:hidden}

  /* Back cover */
  .page--contact{background:var(--green);display:flex;flex-direction:column;align-items:center;padding-top:165px}
  .brand-name{font-weight:800;font-size:78px;letter-spacing:2px;line-height:1}
  .contact{margin-top:28px;text-align:center;font-weight:700}
  .contact__cta{font-size:30px;letter-spacing:1px}
  .contact__phone{font-size:34px;margin-top:4px;letter-spacing:1px}
  .contact__line{display:flex;align-items:center;justify-content:center;gap:14px;font-size:32px;margin-top:8px}
  .contact__icon{width:34px;height:34px;flex:none}

  /* Front cover */
  .page--front{background:var(--navy)}
  .hero-photo{position:absolute;left:0;top:0;width:540px;height:430px;
    background:
      linear-gradient(to bottom,rgba(11,31,138,0) 55%,var(--navy) 100%),
      radial-gradient(circle at 70% 62%,rgba(70,200,160,.55) 0,rgba(70,200,160,0) 22%),
      linear-gradient(135deg,var(--photo-b) 0%,var(--photo-a) 55%,var(--navy-deep) 100%)}
  .page--front .brand-name{position:absolute;top:70px;left:0;width:100%;text-align:center;font-size:86px}

  .highlights{position:absolute;left:28px;top:360px;list-style:none}
  .highlight{position:relative;display:flex;align-items:center;width:480px;min-height:54px;margin-bottom:10px;
    background:var(--green);border-radius:0 27px 27px 0;margin-left:32px;padding:6px 20px 6px 46px;
    font-weight:700;font-size:18px;line-height:1.2}
  .highlight--tall{min-height:64px}
  .highlight__badge{position:absolute;left:-32px;top:50%;transform:translateY(-50%);width:64px;height:64px;border-radius:50%;
    background:var(--green);border:4px solid var(--white);display:flex;align-items:center;justify-content:center}
  .highlight__badge svg{width:30px;height:30px}
</style>
</head>
<body>
<main class="spread">

  <section class="page page--contact">
    <div class="brand-name">WFOL</div>
    <div class="contact">
      <div class="contact__cta">CALL NOW</div>
      <div class="contact__phone">555-014-2871</div>
      <div class="contact__line">
        <svg class="contact__icon" viewBox="0 0 34 34" fill="none" stroke="#fff" stroke-width="2"><rect x="3" y="8" width="28" height="18"/><path d="M3 8l14 11 14-11"/></svg>
        sales@gowfol.com
      </div>
      <div class="contact__line">
        <svg class="contact__icon" viewBox="0 0 34 34" fill="none" stroke="#fff" stroke-width="2"><circle cx="17" cy="17" r="13"/><ellipse cx="17" cy="17" rx="6" ry="13"/><path d="M4 17h26M6 10h22M6 24h22"/></svg>
        www.gowfol.com
      </div>
    </div>
  </section>

  <section class="page page--front">
    <div class="hero-photo" role="img" aria-label="Photo: IT consultants reviewing a dashboard on a computer monitor in a modern office"></div>
    <div class="brand-name">WFOL</div>

    <ul class="highlights">
      <li class="highlight highlight--tall">
        <span class="highlight__badge"><svg viewBox="0 0 30 30" fill="none" stroke="#fff" stroke-width="2"><path d="M6 15l6 6 12-12"/></svg></span>
        No contract / we earn your business on a month to month basis
      </li>
      <li class="highlight">
        <span class="highlight__badge"><svg viewBox="0 0 30 30" fill="none" stroke="#fff" stroke-width="2"><path d="M4 15L15 4h11v11L15 26z"/><circle cx="21" cy="9" r="2"/></svg></span>
        Affordable pricing
      </li>
      <li class="highlight">
        <span class="highlight__badge"><svg viewBox="0 0 30 30" fill="none" stroke="#fff" stroke-width="2"><circle cx="15" cy="15" r="11"/><path d="M15 8v7l5 3"/></svg></span>
        Fast response times
      </li>
      <li class="highlight">
        <span class="highlight__badge"><svg viewBox="0 0 30 30" fill="none" stroke="#fff" stroke-width="2"><path d="M8 5c4 0 5 2 7 2s3-2 7-2c4 0 5 5 3 10-1 3-2 11-5 11s-2-7-5-7-2 7-5 7-4-8-5-11C3 10 4 5 8 5z"/></svg></span>
        25+ local dental practices
      </li>
      <li class="highlight">
        <span class="highlight__badge"><svg viewBox="0 0 30 30" fill="none" stroke="#fff" stroke-width="2"><rect x="7" y="4" width="16" height="22"/><path d="M11 10h8M11 15h8M11 20h5"/></svg></span>
        Predictable fixed-rate billing
      </li>
    </ul>
  </section>

</main>
</body>
</html>
```